Software Platform/Architecture Drawing for website

We need a drawing of a software platform/application.

We are looking for someone to take these abstract concepts and put them into a concrete illustration style. Use the image as baseline description of the framework, not as a template.
See image attached.

The drawing should show the connections between the platform sections, and show that the platform is secure. Platform components can be presented with words or symbols.

There are 2 examples attached to show what kind of graphic we are looking for. Please do not re-create the provided platform drawing in the same concept. We are looking for something more creative to present to our clients.

Thank you.

Industry/Entity Type

Healthcare

Colors

Designer to choose colors to be used in the design.

Requirements
Must have
• the components (not lanes) shown in the KT Platform.pdf design file.
Should not have
• Please do not follow the same 4-lane concept shown in the attached example. This is an example to show the relationship between the lanes and components. The outside design should not follow the same layout.

```html
<!DOCTYPE html>
<html lang="en">
<head>
<meta charset="utf-8">
<title>KT Platform – Secure Platform Architecture</title>
<link href="https://fonts.googleapis.com/css2?family=Roboto:wght@500;700;900&family=Roboto+Condensed:wght@900&display=swap" rel="stylesheet">
<style>
  :root{
    --bg:#0b6db3;
    --bg-deep:#08578f;
    --line:#ffffff;
    --tile-a:#1583e6;
    --tile-b:#25c3f6;
    --tile-edge:#0e5fae;
    --icon-blue:#1d9bf0;
    --callout-text:#222222;
  }
  html,body{margin:0;padding:0;width:1200px;height:845px;overflow:hidden;background:var(--bg);}
  .architecture{display:block;width:1200px;height:845px;}
  .cluster{fill:rgba(255,255,255,0.04);stroke:var(--line);stroke-width:3;}
  .core{fill:rgba(255,255,255,0.08);stroke:var(--line);stroke-width:3;}
  .secure-boundary{fill:none;stroke:var(--line);stroke-width:3.5;stroke-dasharray:1 7;stroke-linecap:round;}
  .item-label{font-family:"Roboto",sans-serif;font-weight:700;font-size:12.5px;fill:var(--line);text-anchor:middle;}
  .callout-box{fill:#ffffff;}
  .callout-pointer{stroke:#ffffff;stroke-width:2.5;}
  .callout-text{font-family:"Roboto",sans-serif;font-weight:500;font-size:17px;fill:var(--callout-text);text-anchor:middle;}
  .anchor-dot{fill:#ffffff;}
  .title{font-family:"Roboto",sans-serif;font-weight:900;font-size:46px;fill:#ffffff;letter-spacing:1px;}
  .secure-title{font-family:"Roboto Condensed",sans-serif;font-weight:900;font-size:72px;fill:#ffffff;}
  .secure-shadow{fill:var(--bg-deep);}
  .flow{fill:none;stroke:var(--line);stroke-width:3.5;stroke-linecap:round;}
  .flow-dotted{fill:none;stroke:var(--line);stroke-width:3.5;stroke-dasharray:1 7;stroke-linecap:round;}
  .icon-disc{fill:#ffffff;}
  .icon-blue{fill:var(--icon-blue);}
  .icon-white{fill:#ffffff;}
  .icon-line{fill:none;stroke:var(--icon-blue);stroke-width:2.5;}
  .icon-text{font-family:"Roboto",sans-serif;font-weight:700;fill:var(--icon-blue);text-anchor:middle;}
</style>
</head>
<body>
<svg class="architecture" viewBox="0 0 1200 845" xmlns="http://www.w3.org/2000/svg">
  <defs>
    <linearGradient id="tileGradient" x1="0" y1="0" x2="1" y2="0">
      <stop offset="0" stop-color="var(--tile-a)"/>
      <stop offset="1" stop-color="var(--tile-b)"/>
    </linearGradient>
    <linearGradient id="figureGradient" x1="0" y1="0" x2="0" y2="1">
      <stop offset="0" stop-color="#ffffff"/>
      <stop offset="1" stop-color="#dceefc"/>
    </linearGradient>
    <marker id="arrowHead" viewBox="0 0 10 10" refX="6" refY="5" markerWidth="4" markerHeight="4" orient="auto">
      <path d="M0,0 L10,5 L0,10 z" fill="#ffffff"/>
    </marker>
  </defs>

  <!-- Title -->
  <text class="title" x="830" y="100">KT PLATFORM</text>

  <!-- Secure platform lettering -->
  <g class="secure-mark">
    <g transform="translate(110,625) rotate(20)">
      <text class="secure-title secure-shadow" x="3" y="6">SECURE</text>
      <text class="secure-title" x="0" y="0">SECURE</text>
    </g>
    <g transform="translate(60,705) rotate(20)">
      <text class="secure-title secure-shadow" x="3" y="6">PLATFORM</text>
      <text class="secure-title" x="0" y="0">PLATFORM</text>
    </g>
  </g>

  <!-- Hub: secure core with orbiting clusters -->
  <ellipse class="secure-boundary" cx="610" cy="500" rx="215" ry="118"/>
  <ellipse class="core" cx="610" cy="500" rx="170" ry="90"/>
  <ellipse class="cluster" cx="330" cy="290" rx="200" ry="105"/>
  <ellipse class="cluster" cx="950" cy="280" rx="200" ry="100"/>
  <ellipse class="cluster" cx="860" cy="690" rx="175" ry="90"/>

  <!-- Flows -->
  <path class="flow" d="M188,188 L228,224" marker-end="url(#arrowHead)"/>
  <path class="flow" d="M468,362 L518,414" marker-end="url(#arrowHead)"/>
  <path class="flow-dotted" d="M768,452 L826,376"/>
  <path class="flow-dotted" d="M722,572 L756,610"/>
  <path class="flow" d="M1040,740 L1008,728" marker-end="url(#arrowHead)"/>

  <!-- Consumer / Patient tile -->
  <g class="tile-consumer">
    <polygon points="35,160 120,112 205,160 120,208" fill="var(--tile-edge)"/>
    <polygon points="35,150 120,102 205,150 120,198" fill="url(#tileGradient)"/>
    <rect role="img" aria-label="Group of patients" x="78" y="88" width="84" height="66" rx="22" fill="url(#figureGradient)"/>
  </g>

  <!-- Administrators tile -->
  <g class="tile-admin">
    <polygon points="1025,770 1110,722 1195,770 1110,818" fill="var(--tile-edge)"/>
    <polygon points="1025,760 1110,712 1195,760 1110,808" fill="url(#tileGradient)"/>
    <rect role="img" aria-label="Administrator with settings gear" x="1075" y="688" width="70" height="70" rx="22" fill="url(#figureGradient)"/>
  </g>

  <!-- Patient interaction -->
  <g class="patient-items">
    <circle class="icon-disc" cx="205" cy="265" r="20"/>
    <polygon class="icon-blue" points="193,266 205,254 217,266 214,266 214,278 196,278 196,266"/>
    <text class="item-label" x="205" y="303">Home</text>
    <text class="item-label" x="205" y="318">Devices</text>

    <circle class="icon-disc" cx="268" cy="265" r="20"/>
    <path class="icon-blue" d="M268,276 l-10,-10 a6,6 0 0 1 10,-7 a6,6 0 0 1 10,7 z"/>
    <text class="item-label" x="268" y="303">Wearable</text>
    <text class="item-label" x="268" y="318">Devices</text>

    <circle class="icon-disc" cx="330" cy="265" r="20"/>
    <circle class="icon-line" cx="330" cy="265" r="12"/>
    <ellipse class="icon-line" cx="330" cy="265" rx="5" ry="12"/>
    <path class="icon-line" d="M318,265 h24"/>
    <text class="item-label" x="330" y="303">Web</text>

    <circle class="icon-disc" cx="392" cy="265" r="20"/>
    <rect class="icon-blue" x="382" y="255" width="8" height="8" rx="1.5"/>
    <rect class="icon-blue" x="394" y="255" width="8" height="8" rx="1.5"/>
    <rect class="icon-blue" x="382" y="267" width="8" height="8" rx="1.5"/>
    <rect class="icon-blue" x="394" y="267" width="8" height="8" rx="1.5"/>
    <text class="item-label" x="392" y="303">Apps</text>

    <circle class="icon-disc" cx="455" cy="265" r="20"/>
    <text class="icon-text" x="455" y="270" font-size="12">sms</text>
    <text class="item-label" x="455" y="303">SMS</text>
  </g>

  <!-- Services core -->
  <g class="service-items">
    <circle class="icon-disc" cx="530" cy="478" r="20"/>
    <rect class="icon-blue" x="522" y="478" width="16" height="11" rx="2"/>
    <path class="icon-line" d="M525,478 v-4 a5,5 0 0 1 10,0 v4"/>
    <text class="item-label" x="530" y="517">Identity &amp;</text>
    <text class="item-label" x="530" y="532">access control</text>

    <circle class="icon-disc" cx="610" cy="468" r="20"/>
    <path class="icon-blue" d="M598,460 v16 a12,4 0 0 0 24,0 v-16z"/>
    <ellipse class="icon-white" cx="610" cy="460" rx="12" ry="4"/>
    <text class="item-label" x="610" y="507">Database</text>

    <circle class="icon-disc" cx="690" cy="478" r="20"/>
    <circle class="icon-blue" cx="686" cy="476" r="6"/>
    <circle class="icon-blue" cx="695" cy="483" r="4"/>
    <text class="item-label" x="690" y="517">Logic</text>
  </g>

  <!-- External connections -->
  <g class="external-items">
    <circle class="icon-disc" cx="810" cy="265" r="20"/>
    <text class="icon-text" x="810" y="269" font-size="11">SOC</text>
    <text class="item-label" x="810" y="303">Social</text>
    <text class="item-label" x="810" y="318">media</text>

    <circle class="icon-disc" cx="880" cy="265" r="20"/>
    <rect class="icon-blue" x="869" y="256" width="22" height="15" rx="2"/>
    <rect class="icon-blue" x="876" y="273" width="8" height="3"/>
    <text class="item-label" x="880" y="303">Hub</text>
    <text class="item-label" x="880" y="318">systems</text>

    <circle class="icon-disc" cx="950" cy="265" r="20"/>
    <text class="icon-text" x="950" y="272" font-size="20">@</text>
    <text class="item-label" x="950" y="303">E-mail</text>

    <circle class="icon-disc" cx="1020" cy="265" r="20"/>
    <circle class="icon-blue" cx="1020" cy="264" r="6"/>
    <path class="icon-line" d="M1010,266 a10,10 0 0 1 20,0"/>
    <text class="item-label" x="1020" y="303">Call</text>
    <text class="item-label" x="1020" y="318">center</text>

    <circle class="icon-disc" cx="1090" cy="265" r="20"/>
    <path class="icon-blue" d="M1086,254 h8 v7 h7 v8 h-7 v7 h-8 v-7 h-7 v-8 h7z"/>
    <text class="item-label" x="1090" y="303">EHR</text>
  </g>

  <!-- Output -->
  <g class="output-items">
    <circle class="icon-disc" cx="780" cy="668" r="20"/>
    <rect class="icon-blue" x="771" y="668" width="4" height="8"/>
    <rect class="icon-blue" x="778" y="662" width="4" height="14"/>
    <rect class="icon-blue" x="785" y="658" width="4" height="18"/>
    <text class="item-label" x="780" y="707">Client</text>
    <text class="item-label" x="780" y="722">dashboard</text>

    <circle class="icon-disc" cx="860" cy="668" r="20"/>
    <circle class="icon-blue" cx="855" cy="665" r="5"/>
    <circle class="icon-blue" cx="866" cy="672" r="4"/>
    <text class="item-label" x="860" y="707">Admin</text>
    <text class="item-label" x="860" y="722">Portal</text>

    <circle class="icon-disc" cx="940" cy="668" r="20"/>
    <circle class="icon-line" cx="940" cy="668" r="11"/>
    <ellipse class="icon-line" cx="940" cy="668" rx="4.5" ry="11"/>
    <text class="item-label" x="940" y="707">Web</text>
    <text class="item-label" x="940" y="722">Portal</text>
  </g>

  <!-- Callouts -->
  <g class="callouts">
    <line class="callout-pointer" x1="245" y1="88" x2="178" y2="122"/>
    <polygon class="callout-box" points="238,40 388,40 380,92 230,92"/>
    <circle class="anchor-dot" cx="178" cy="122" r="5"/>
    <text class="callout-text" x="309" y="62">Consumer/</text>
    <text class="callout-text" x="309" y="83">Patient</text>

    <line class="callout-pointer" x1="455" y1="168" x2="470" y2="215"/>
    <polygon class="callout-box" points="448,118 598,118 590,170 440,170"/>
    <circle class="anchor-dot" cx="470" cy="215" r="5"/>
    <text class="callout-text" x="519" y="140">Patient</text>
    <text class="callout-text" x="519" y="161">Interaction</text>

    <line class="callout-pointer" x1="590" y1="358" x2="620" y2="383"/>
    <polygon class="callout-box" points="566,320 696,320 688,358 558,358"/>
    <circle class="anchor-dot" cx="620" cy="383" r="5"/>
    <text class="callout-text" x="627" y="345">Services</text>

    <line class="callout-pointer" x1="850" y1="175" x2="900" y2="190"/>
    <polygon class="callout-box" points="768,125 918,125 910,175 760,175"/>
    <circle class="anchor-dot" cx="900" cy="190" r="5"/>
    <text class="callout-text" x="839" y="146">External</text>
    <text class="callout-text" x="839" y="167">Connections</text>

    <line class="callout-pointer" x1="990" y1="175" x2="990" y2="182"/>
    <polygon class="callout-box" points="938,125 1058,125 1050,175 930,175"/>
    <circle class="anchor-dot" cx="990" cy="182" r="5"/>
    <text class="callout-text" x="994" y="146">3rd party</text>
    <text class="callout-text" x="994" y="167">APIs</text>

    <line class="callout-pointer" x1="950" y1="585" x2="960" y2="618"/>
    <polygon class="callout-box" points="938,545 1048,545 1040,585 930,585"/>
    <circle class="anchor-dot" cx="960" cy="618" r="5"/>
    <text class="callout-text" x="989" y="571">Output</text>

    <line class="callout-pointer" x1="1110" y1="660" x2="1125" y2="690"/>
    <polygon class="callout-box" points="1068,620 1196,620 1188,660 1060,660"/>
    <circle class="anchor-dot" cx="1125" cy="690" r="5"/>
    <text class="callout-text" x="1128" y="646">Administrators</text>
  </g>
</svg>
</body>
</html>
```